K&T Smokehouse Website Design Project

K& T Smokehouse AsadorÃa is a fast-casual restaurant that specializes in southern culture, soul food, baby back ribs and bourbon whiskey.
We need a functional and user friendly website design for our customers to be able to explore our menu options, learn about our culture, as well as be able to place and pay for online orders that can be picked up at the nearest restaurant. Benchmarks for our website are www.velmorbakes.example, www.quarnito.example and www.surelapeak.example
The site design should also serve as an initial point of contact for prospective franchisees to dig and learn about the brand and business opportunity.
We want customers (consumers and potential franchisees) to be able to experience FIRST THE FOOD, but also the style and culture of our restaurants via the website design. Key elements for this are: soul food (Fill Every Plate), southern culture, friendly service, bluegrass/folk music, bourbon/moonshine/Tennessee whisky, modern butcher-shop design as well as industrial, wood, modern rustic, organic elements. (see restaurant images of tile, concrete, vintage scales, green wall, etc)
We want the website to provide a good overall brand image and also drive participation and sales by via images of our food, by these images being at front and center of the website design. See benchmark websites (Velmor, Surela Peak, Quarnito) for good examples of this.
Other elements to take under consideration for the website design are:
* Illustrative but simple menu
* Hacer un pedido (order online), Loyalty Program and Franquicias sections should have different, separate and easy to see buttons in the homepage.
* Simple, but modern functionality overall for the website.
* Respect colors and elements of the brand (attached some photos and examples)
* Brand Typography included (NAMES OF TYPOGRAPHY: BEBAS, SONGBIRD, CANTER & VAST SHADOW)
Minimum Deliverables: Home Page, Menu and Order Online. 3 pages total.
• More examples can be found at: www.facebook.com/ktsmokehouseasadoria
• Website architecture / Site Map ATTACHED
* More design elements attached.
* Screenshots of some good elements to take under consideration for website functionality and design.
- BEBAS, SONGBRID, CANTER & VAST SHADOW

```html
<!DOCTYPE html>
<html lang="en">
<head>
<meta charset="utf-8">
<title>K&amp;T Smokehouse</title>
<link href="https://fonts.googleapis.com/css2?family=Bebas+Neue&family=Arimo:wght@400;700&display=swap" rel="stylesheet">
<style>
:root{
  --cream:#f2e4c4;
  --cream-light:#f6ecd6;
  --tan:#bba882;
  --black:#0c0c0c;
  --lime:#c8ea17;
  --peach:#f4dcbd;
  --accent:#c0420f;
  --tweet-date:#b3290d;
  --orange:#c8702a;
  --ink:#1e1e1e;
  --panel:rgba(236,234,234,.92);
}
*{margin:0;padding:0;box-sizing:border-box}
html,body{width:1200px;height:1148px;overflow:hidden}
body{position:relative;background:var(--cream);font-family:"Arimo",Arial,sans-serif;color:var(--ink)}
.abs{position:absolute}

/* header */
.site-header{left:0;top:0;width:1200px;height:80px;background:linear-gradient(180deg,var(--cream-light),#efe1c2)}
.brand{left:228px;top:4px;height:72px;display:flex;align-items:center;gap:10px}
.brand-mark{width:34px;height:34px;border-radius:50%;background:#222}
.brand-name{font-family:"Bebas Neue",sans-serif;font-size:28px;color:#222;letter-spacing:1px}
.account{left:556px;top:35px;font-size:11px;color:var(--orange)}
.account span{color:#cfb995;margin:0 5px}
.search{left:653px;top:30px;width:157px;height:18px;background:#ece3cc;border:1px solid #e3d7b9;font-size:11px;color:#b8ab8e;padding:2px 10px}
.search svg{position:absolute;right:4px;top:2px}
.quick-actions{left:838px;top:0;width:137px;height:78px;background:#efe3c6;border-left:1px solid #e2d4b1;border-right:1px solid #e2d4b1}
.quick-btn{position:absolute;left:10px;width:113px;height:25px;background:#fbf6ea;border:1px solid #e6d9bd;font-family:Georgia,serif;font-size:13px;color:var(--orange);display:flex;align-items:center;gap:6px;padding-left:4px}
.quick-btn i{width:16px;height:16px;background:var(--accent);border-radius:2px;display:block}

/* nav */
.main-nav{left:0;top:80px;width:1200px;height:45px;background:var(--black)}
.main-nav a{position:absolute;top:16px;font-family:"Bebas Neue",sans-serif;font-size:14px;color:#fff;text-decoration:none;letter-spacing:.5px}

/* hero */
.hero{left:0;top:125px;width:1200px;height:500px;background:
  radial-gradient(ellipse 10% 12% at 38% 88%,rgba(236,206,40,.85),rgba(236,206,40,0) 100%),
  radial-gradient(ellipse 38% 14% at 66% 80%,rgba(112,160,60,.55),rgba(112,160,60,0) 100%),
  radial-gradient(ellipse 40% 26% at 66% 52%,rgba(196,70,38,.95),rgba(150,56,26,.7) 55%,rgba(120,60,30,0) 100%),
  radial-gradient(ellipse 42% 14% at 66% 27%,rgba(150,98,60,.9),rgba(150,98,60,0) 100%),
  radial-gradient(ellipse 16% 30% at 20% 60%,rgba(214,150,72,.85),rgba(214,150,72,0) 100%),
  linear-gradient(180deg,rgba(0,0,0,0) 60%,rgba(214,208,200,.75) 82%,rgba(170,164,158,.7) 100%),
  linear-gradient(180deg,#2a2420 0%,#3b2c22 40%,#4a3a30 100%)}
.menu-cats a{position:absolute;left:225px;width:120px;height:39px;background:var(--lime);font-size:10px;color:#1a1a1a;display:flex;align-items:center;justify-content:center;text-decoration:none}
.menu-cats a.active{background:var(--peach);color:#e8250f}
.submenu{left:368px;top:147px;width:121px;height:304px;background:var(--panel)}
.submenu a{position:absolute;left:0;width:121px;text-align:center;font-size:10px;color:#1a1a1a;text-decoration:none}
.submenu a.active{color:#e8250f}
.hero-note{left:596px;top:225px;width:379px;height:92px;background:rgba(240,236,236,.85);font-size:10px;line-height:17.5px;padding:9px 24px 9px 7px;letter-spacing:.15px;color:#111}

/* feature cards */
.card{top:668px;width:238px;height:265px;background:var(--tan)}
.card h2{font-family:"Bebas Neue",sans-serif;font-size:44px;color:#fff;text-align:center;margin-top:10px;letter-spacing:.5px;text-shadow:1px 1px 0 #6b5a3c,2px 2px 0 #6b5a3c}
.card-photo{position:absolute;border:2px solid #f1e6cf}
.card p{position:absolute;font-size:11px;line-height:15px;text-align:center;color:#2a2418}
.tweet{position:absolute;left:12px;width:218px;font-size:11px;line-height:12px;color:#2a2418}
.tweet b{display:block;font-weight:400;color:var(--tweet-date);letter-spacing:.5px;margin-top:1px}

/* footer */
.site-footer{left:0;top:968px;width:1200px;height:180px;background:linear-gradient(180deg,#f4ead3,#ead9b5);border-top:3px solid #3a3530}
.foot-col{top:26px}
.foot-col h3{font-size:13px;font-weight:400;color:#111;margin-bottom:15px}
.foot-col a{display:block;font-size:10.5px;font-weight:700;color:var(--accent);letter-spacing:.8px;line-height:18.8px;text-decoration:none}
.social{display:flex;gap:6px;margin-top:-2px}
.social i{width:22px;height:22px;background:#b8ad98;border-radius:2px;display:block}
.legal{left:0;top:161px;width:1200px;text-align:center;font-size:9px;color:#222;padding-left:-20px}
</style>
</head>
<body>

<header class="site-header abs">
  <div class="brand abs"><span class="brand-mark"></span><span class="brand-name">K&amp;T Smokehouse</span></div>
  <div class="account abs">Sign In<span>|</span>Join Now</div>
  <div class="search abs">Search
    <svg width="12" height="12" viewBox="0 0 12 12"><circle cx="7.5" cy="4.5" r="3" fill="none" stroke="#c8702a" stroke-width="1.3"/><line x1="5.5" y1="6.5" x2="2" y2="11" stroke="#c8702a" stroke-width="1.5"/></svg>
  </div>
  <div class="quick-actions abs">
    <a class="quick-btn" style="top:8px"><i></i>Order Online</a>
    <a class="quick-btn" style="top:43px"><i></i>Order Catering</a>
  </div>
</header>

<nav class="main-nav abs">
  <a style="left:238px">About Us</a>
  <a style="left:337px">Menu&nbsp; Catering</a>
  <a style="left:470px">Nutrition</a>
  <a style="left:573px">Club Peak</a>
  <a style="left:677px">Franchising</a>
  <a style="left:794px">Gift Cards</a>
  <a style="left:901px">Order Online</a>
</nav>

<section class="hero abs" role="img" aria-label="Photo of a tall bacon, lettuce and tomato sandwich on toasted bread with potato wedges and a yellow tomato on a white plate"></section>

<div class="menu-cats">
  <a style="top:147px">DOWNLOAD MENU</a>
  <a class="active" style="top:190px">BURRITOS</a>
  <a style="top:234px">TACOS &amp; TAQUITOS</a>
  <a style="top:277px">FAVORITES</a>
  <a style="top:322px">SALADS</a>
  <a style="top:367px">SIDES</a>
  <a style="top:412px">KIDS</a>
</div>

<div class="submenu abs">
  <a style="top:12px">BAJA BURRITO</a>
  <a class="active" style="top:56px">BURRITO MEXICANO</a>
  <a style="top:100px">BURRITO ULTIMO</a>
  <a style="top:145px">DIABLE BURRITO</a>
  <a style="top:189px">NACHO BURRITO</a>
  <a style="top:233px">GRILLED VEGGIE</a>
  <a style="top:277px">BURRITO</a>
</div>

<div class="hero-note abs">Lorem ipsum dolor sit amet, consectetur adipiscing elit, sed do eiusmod tempor incididunt ut labore et dolore magna aliqua. Ut enim ad minim veniam, quis nostrud exercitation ullamco laboris nisi ut aliquip ex ea commodo conse-quat. Duis aute irure</div>

<article class="card abs" style="left:222px">
  <h2>Eat Well</h2>
  <div class="card-photo" style="left:15px;top:72px;width:206px;height:102px;background:radial-gradient(ellipse 55% 60% at 45% 50%,#8a3e1a,#4a2210 60%,#d9cfc2 100%)" role="img" aria-label="Photo of grilled meat wrapped in a tortilla"></div>
  <p style="left:8px;top:189px;width:222px">Sed ut perspiciatis unde omnis iste natus error sit voluptatem accusantium doloremque laudantium, totam rem aperiamdicta tur</p>
</article>

<article class="card abs" style="left:479px">
  <h2>Fresh Buzz</h2>
  <div class="tweet" style="top:71px">RT @marenholloway: We need a @boldsurelapeak in #LoveLansing!<b>2.19.15 at 4:02 pm</b></div>
  <div class="tweet" style="top:121px">RT @iAmTovric: Yessssss!!! There's a Surela Peak right by my hotel!!!!<b>2.19.15 at 3:53 pm</b></div>
  <div class="tweet" style="top:171px">@quellbee52 What burrito is your fave?<b>2.19.15 at 3:52 pm</b></div>
  <div class="tweet" style="top:209px">RT @quellbee52: I want a burrito from Surela Peak!<b>2.19.15 at 3:52 pm</b></div>
</article>

<article class="card abs" style="left:736px">
  <h2>Skip The Line</h2>
  <div class="card-photo" style="left:18px;top:72px;width:206px;height:132px;background:radial-gradient(ellipse 45% 40% at 48% 52%,#8d8d8d,#cfcfcf 60%,#ffffff 100%)" role="img" aria-label="Laptop, tablet and phone showing the online ordering site"></div>
  <p style="left:18px;top:213px;width:206px;letter-spacing:.5px">Sed ut perspiciatis unde omnis iste natus error sit voluptatem</p>
</article>

<footer class="site-footer abs">
  <div class="foot-col abs" style="left:227px"><h3>Our Company</h3>
    <a>About Velmor Bread</a><a>Investor Relations</a><a>Press Room</a><a>Franchise Information</a><a>Careers</a>
  </div>
  <div class="foot-col abs" style="left:411px"><h3>How Can We Help?</h3><a>Contact &amp; FAQs</a></div>
  <div class="foot-col abs" style="left:605px"><h3>Gift Cards</h3>
    <a>Send an eGift Card</a><a>Buy a Gift Card</a><a>Gift Cards - Learn More</a><a>Check Your Balance</a>
  </div>
  <div class="foot-col abs" style="left:799px"><h3>Connect</h3>
    <div class="social"><i></i><i></i><i></i><i></i><i></i><i></i></div>
  </div>
  <div class="legal abs" style="left:-16px">Copyright©2015 . All rights reserved. Terms of Use Your Privacy</div>
</footer>

</body>
</html>
```